Business card design and logo for plumbing bussiness

We are wanting a logo for a plumbing business is Queensland Australia. KLV Plumbing and Drainage will be doing works on domestic and commercial sites.
Plumbing, drainage and gas works. We are wanting something that will stand out and be noticed. Colours could be black blue and white but open for suggestions.

Target Market(s)

Builders and home renovators

Industry/Entity Type

Plumbing

Contact Information for Business Card

Dorian Machell - Director
0417 582 031
dorian@klvplumbing-example.com.au
QBCC: 374 8106
ABN: 52 913 207 615

Font styles to use
Sans Serif

Colors
000000

Requirements
Must have
• Clear defined branding

```html
<!DOCTYPE html>
<html lang="en">
<head>
<meta charset="utf-8">
<title>KLV Plumbing and Drainage — Business Card</title>
<link rel="stylesheet" href="https://fonts.googleapis.com/css2?family=Oswald:wght@400&family=Roboto:wght@400&display=swap">
<style>
  :root {
    --stage: #e4e1dc;
    --card: #1b1b1c;
    --card-edge: #232324;
    --blue: #1ab4ea;
    --blue-deep: #1c5f9a;
    --white: #f4f6f8;
    --muted: #d9dde1;
  }
  * { box-sizing: border-box; margin: 0; padding: 0; }
  html, body {
    width: 1200px; height: 1000px; overflow: hidden;
    background: var(--stage);
  }
  .canvas { position: relative; width: 1200px; height: 1000px; }

  .card {
    position: absolute; left: 270px; width: 662px;
    background: linear-gradient(180deg, var(--card-edge), var(--card));
    box-shadow: 0 6px 18px rgba(0,0,0,0.25);
  }
  .card--front { top: 88px; height: 378px; }
  .card--back  { top: 520px; height: 382px; }

  .brand {
    position: absolute;
    font-family: "Oswald", sans-serif; font-weight: 400;
    color: var(--white); text-transform: uppercase; text-align: center;
    display: flex; align-items: center; gap: 12px;
  }
  .brand__dot {
    width: 18px; height: 18px; border-radius: 50%;
    background: var(--blue); flex: none;
  }
  .card--front .brand {
    left: 0; right: 0; top: 160px; justify-content: center;
    font-size: 34px; letter-spacing: 1px;
  }
  .card--back .brand {
    left: 80px; width: 240px; top: 110px;
    flex-direction: column; gap: 14px;
    font-size: 22px; line-height: 1.25;
  }

  .divider {
    position: absolute; left: 330px; top: 122px; width: 1px; height: 152px;
    background: linear-gradient(180deg, transparent, var(--blue-deep), transparent);
  }

  .contact {
    position: absolute; left: 364px; top: 104px;
    font-family: "Roboto", sans-serif; color: var(--white);
  }
  .contact__name { font-size: 18px; color: var(--blue); line-height: 22px; }
  .contact__role { font-size: 14px; line-height: 20px; margin-bottom: 14px; }
  .contact__list { list-style: none; }
  .contact__item {
    display: flex; align-items: center; gap: 6px;
    font-size: 14.5px; line-height: 21.5px;
  }
  .contact__icon { width: 11px; height: 11px; flex: none; }
  .contact__reg { margin-top: 10px; font-size: 14.5px; line-height: 21px; }
</style>
</head>
<body>
<main class="canvas">
  <section class="card card--front" aria-label="Business card front">
    <div class="brand"><span class="brand__dot"></span>KLV Plumbing &amp; Drainage</div>
  </section>

  <section class="card card--back" aria-label="Business card back">
    <div class="brand"><span class="brand__dot"></span><span>KLV<br>Plumbing &amp; Drainage</span></div>
    <div class="divider"></div>
    <div class="contact">
      <p class="contact__name">Dorian Machell</p>
      <p class="contact__role">Director</p>
      <ul class="contact__list">
        <li class="contact__item">
          <svg class="contact__icon" viewBox="0 0 12 12" aria-hidden="true"><path d="M2.5 1 L4.5 3.2 L3.5 4.5 Q5 7.2 7.5 8.5 L8.8 7.5 L11 9.5 L9.8 11 Q4.5 10.5 1 2.2 Z" fill="var(--blue)"/></svg>
          0417 582 031
        </li>
        <li class="contact__item">
          <svg class="contact__icon" viewBox="0 0 12 12" aria-hidden="true"><rect x="0.5" y="2.5" width="11" height="7.5" fill="var(--blue)"/><path d="M0.5 2.5 L6 6.8 L11.5 2.5" stroke="var(--card)" stroke-width="1" fill="none"/></svg>
          dorian@klvplumbing-example.com.au
        </li>
        <li class="contact__item">
          <svg class="contact__icon" viewBox="0 0 12 12" aria-hidden="true"><g fill="none" stroke="var(--blue)" stroke-width="1"><circle cx="6" cy="6" r="5"/><ellipse cx="6" cy="6" rx="2.2" ry="5"/><path d="M1 6 H11"/></g></svg>
          www.klvplumbing-example.com.au
        </li>
      </ul>
      <p class="contact__reg">QBCC: 374 8106<br>ABN: 52 913 207 615</p>
    </div>
  </section>
</main>
</body>
</html>
```